Thank you for shopping with us business card

We would like a thank you card for our rebranded business. We used to be "Brindle Goods" but are now "Marlow Finds. Old thank you card and new logo will be attached for reference. New thank you card does not have to be same design as old thank you card, but please use new logo.
Shopmart URL is now marlowfinds.shopmart.example
Instagram is @Marlow_Finds
Email is marlowfinds@mailbox.example
Thank you!

Contact Information for Business Card

Shopmart site, email, Instagram

```html
<!DOCTYPE html>
<html lang="en">
<head>
<meta charset="utf-8">
<title>Marlow Finds – Thank You Card</title>
<link rel="stylesheet" href="https://fonts.googleapis.com/css2?family=Open+Sans:wght@700;800&display=swap">
<style>
  :root {
    --backdrop: #444444;
    --card-white: #ffffff;
    --card-fade: #ececec;
    --accent-orange: #f09000;
    --ink: #1b1b1b;
    --mark-grey: #cfcfcf;
  }
  * { margin: 0; padding: 0; box-sizing: border-box; }
  html, body {
    width: 1200px;
    height: 900px;
    overflow: hidden;
    background: var(--backdrop);
    font-family: "Open Sans", sans-serif;
  }
  .thank-you-card {
    position: absolute;
    left: 40px;
    top: 130px;
    width: 1120px;
    height: 640px;
    background: linear-gradient(170deg, var(--card-white) 55%, var(--card-fade) 100%);
    overflow: hidden;
  }
  .band-orange {
    position: absolute;
    left: 0; top: 0;
    width: 150px; height: 100%;
    background: var(--accent-orange);
  }
  .band-black {
    position: absolute;
    left: 150px; top: 0;
    width: 52px; height: 100%;
    background: var(--ink);
  }
  .brand-mark {
    position: absolute;
    right: 30px;
    top: 40px;
    font-weight: 800;
    font-size: 30px;
    line-height: 1.05;
    text-align: center;
    color: var(--mark-grey);
  }
  .headline {
    position: absolute;
    left: 280px;
    top: 60px;
    font-weight: 800;
    font-size: 54px;
    line-height: 1.02;
    letter-spacing: -0.5px;
    color: var(--ink);
    text-transform: uppercase;
  }
  .headline-swoosh {
    position: absolute;
    left: 285px;
    top: 185px;
    width: 470px;
    height: 14px;
  }
  .message {
    position: absolute;
    left: 285px;
    top: 275px;
    width: 720px;
    font-weight: 700;
    font-size: 30px;
    line-height: 1.3;
    color: var(--ink);
  }
  .contact-list {
    position: absolute;
    left: 288px;
    top: 480px;
    list-style: none;
  }
  .contact-item {
    display: flex;
    align-items: center;
    gap: 22px;
    height: 52px;
    font-weight: 700;
    font-size: 30px;
    color: var(--ink);
  }
  .contact-icon {
    width: 38px;
    height: 38px;
    flex: none;
  }
</style>
</head>
<body>
  <section class="thank-you-card">
    <div class="band-orange"></div>
    <div class="band-black"></div>

    <div class="brand-mark">Marlow<br>Finds</div>

    <h1 class="headline">Thank you for<br>your purchase</h1>
    <svg class="headline-swoosh" viewBox="0 0 470 14" aria-hidden="true">
      <path d="M0 12 Q230 2 470 0 Q235 7 0 14 Z" fill="var(--ink)"/>
    </svg>

    <p class="message">Your purchase made my day and I hope this package brightens yours. Please come back and leave a review!</p>

    <ul class="contact-list">
      <li class="contact-item">
        <svg class="contact-icon" viewBox="0 0 38 38" aria-hidden="true">
          <rect x="5" y="5" width="28" height="28" fill="none" stroke="var(--ink)" stroke-width="4"/>
        </svg>
        <span>@Marlow_Finds</span>
      </li>
      <li class="contact-item">
        <svg class="contact-icon" viewBox="0 0 38 38" aria-hidden="true">
          <rect x="2" y="8" width="34" height="23" fill="var(--ink)"/>
          <path d="M2 8 L19 22 L36 8" fill="none" stroke="var(--card-white)" stroke-width="2.5"/>
          <path d="M2 31 L15 19 M36 31 L23 19" stroke="var(--card-white)" stroke-width="2"/>
        </svg>
        <span>marlowfinds@mailbox.example</span>
      </li>
      <li class="contact-item">
        <svg class="contact-icon" viewBox="0 0 38 38" aria-hidden="true">
          <g fill="none" stroke="var(--ink)" stroke-width="3">
            <circle cx="19" cy="19" r="15"/>
            <ellipse cx="19" cy="19" rx="7" ry="15"/>
            <line x1="4" y1="19" x2="34" y2="19"/>
            <line x1="19" y1="4" x2="19" y2="34"/>
            <path d="M7 11 H31 M7 27 H31"/>
          </g>
        </svg>
        <span>marlowfinds.shopmart.example</span>
      </li>
    </ul>
  </section>
</body>
</html>
```